HCF Package
Church letterhead, envelopes and business card
Creative Brief
Use specific fonts
Friz Quadrata & Rage Italics LET
Cutting-Edge
The Harborview Fellowship
218 Maple Crest Lane Newport News, VA 23607
info@hcfnet.example
www.theharborviewfellowship.example
Dalton M. Whitley, Lead Pastor Service Schedule: Sunday Christian Training: 10:00 am Sunday Worship Service: 11:15 am Sunday Celebration Service: 6:30 pm Connection Groups (weekdays): 7:00 pm -Children and Student activities provided -Nursery provided ***NOTE*** We currently have all the above information on the front of the card. We also have a small map to the church as well as Facebook & Twitter logos and lines for writing on the back, but we're leaving it up to you to place things where you think best. Also, we currently use Pantone colors 519 (deep plum) and 5773 (olive green). We are interested in possibly having either green or purple foil on the letterhead, envelopes and business card too.

```html
<!DOCTYPE html>
<html lang="en">
<head>
<meta charset="utf-8">
<title>HCF Stationery</title>
<link href="https://fonts.googleapis.com/css2?family=Marcellus&family=Open+Sans:wght@400;600&display=swap" rel="stylesheet">
<style>
  :root {
    --plum: #5a2f5f;
    --olive: #9aa176;
    --olive-light: #d9dcc3;
    --ink: #3d3a3d;
    --muted: #8a878a;
    --rule: #c9c7c9;
    --paper: #ffffff;
    --backdrop: #ecebe6;
    --faint: #ecebee;
  }
  * { box-sizing: border-box; margin: 0; padding: 0; }
  html, body { width: 1200px; height: 935px; overflow: hidden; }
  body {
    position: relative;
    background: var(--backdrop);
    font-family: "Open Sans", Arial, sans-serif;
    color: var(--ink);
  }
  .sheet {
    position: absolute;
    background: var(--paper);
    box-shadow: 0 2px 8px rgba(0,0,0,.18);
    overflow: hidden;
  }
  .brand {
    display: flex; align-items: center; gap: 8px;
    font-family: "Marcellus", serif;
    color: var(--plum);
    white-space: nowrap;
  }
  .brand .mark { width: 14px; height: 14px; border-radius: 50%; background: var(--plum); flex: none; }
  .footer-art {
    position: absolute; left: 0; right: 0; bottom: 0;
    background: linear-gradient(to top, var(--faint), rgba(236,235,238,0));
  }
  .address { position: absolute; font-size: 11px; line-height: 1.55; color: var(--ink); white-space: nowrap; z-index: 1; }
  .address b { font-weight: 600; color: var(--plum); }

  /* Fax (back) */
  .fax { left: 45px; top: 165px; width: 590px; height: 760px; z-index: 1; }
  .fax .brand { position: absolute; left: 22px; top: 40px; font-size: 22px; }
  .fax h1 { position: absolute; left: 22px; top: 140px; font-family: "Marcellus", serif; font-weight: 400; font-size: 36px; letter-spacing: 1px; }
  .fax .fields { position: absolute; left: 22px; top: 200px; width: 120px; list-style: none; }
  .fax .fields li { display: flex; gap: 8px; font-size: 11px; height: 36px; align-items: flex-end; }
  .fax .fields li span:last-child { flex: 1; border-bottom: 1px dotted var(--muted); }
  .fax .checks { position: absolute; left: 22px; top: 438px; display: flex; gap: 22px; font-size: 10px; color: var(--muted); }
  .fax .checks span::before { content: ""; display: inline-block; width: 9px; height: 9px; border: 1px solid var(--muted); background: #eee; margin-right: 5px; vertical-align: -1px; }
  .fax .address { left: 22px; top: 682px; }
  .fax .footer-art { height: 130px; }

  /* Letterhead (middle) */
  .letterhead { left: 190px; top: 38px; width: 585px; height: 800px; z-index: 2; }
  .letterhead .brand { position: absolute; left: 62px; top: 32px; font-size: 26px; }
  .letterhead .side-rule { position: absolute; top: 0; bottom: 0; left: 545px; width: 3px; background: var(--rule); }
  .letterhead .address { left: 40px; top: 728px; }
  .letterhead .footer-art { height: 120px; }

  /* Envelope (front) */
  .envelope { left: 526px; top: 240px; width: 632px; height: 430px; z-index: 3; }
  .envelope .flap { position: absolute; left: 0; top: 0; width: 100%; height: 63px; background: linear-gradient(to bottom, var(--olive) 0%, #b8bd97 60%, var(--olive-light) 100%); }
  .envelope .brand { position: absolute; left: 24px; top: 95px; font-size: 24px; }
  .envelope .address { left: 24px; top: 300px; }
  .envelope .footer-art { left: auto; width: 230px; height: 170px; }

  /* Business card front */
  .card-front { left: 835px; top: 63px; width: 223px; height: 139px; z-index: 4; border-radius: 6px; }
  .card-front .person { position: absolute; left: 14px; top: 12px; font-size: 10px; line-height: 1.35; }
  .card-front .person b { color: var(--plum); font-weight: 600; }
  .card-front .brand { position: absolute; right: 14px; top: 48px; font-size: 11px; gap: 5px; }
  .card-front .brand .mark { width: 8px; height: 8px; }
  .card-front .contact { position: absolute; left: 14px; top: 90px; font-size: 7px; line-height: 1.55; white-space: nowrap; }

  /* Business card back */
  .card-back { left: 923px; top: 632px; width: 228px; height: 190px; z-index: 4; border-radius: 6px; }
  .card-back .brand { position: absolute; right: 12px; top: 14px; font-size: 10px; gap: 4px; }
  .card-back .brand .mark { width: 7px; height: 7px; }
  .card-back .schedule { position: absolute; left: 12px; top: 44px; width: 204px; font-size: 6.5px; line-height: 1.75; list-style: none; white-space: nowrap; }
  .card-back .schedule .head { font-weight: 600; color: var(--plum); }
  .card-back .schedule li.line { border-bottom: 1px solid var(--rule); }
</style>
</head>
<body>

<section class="sheet fax" aria-label="Fax cover sheet">
  <div class="brand"><span class="mark"></span>The Harborview Fellowship</div>
  <h1>FAX</h1>
  <ul class="fields">
    <li><span>To :</span><span></span></li>
    <li><span>Fax :</span><span></span></li>
    <li><span>Phone :</span><span></span></li>
    <li><span>Re :</span><span></span></li>
  </ul>
  <div class="checks"><span>Urgent</span><span>For Review</span></div>
  <p class="address">218 Maple Crest Lane Alder Cove, OR 97999<br>
    <b>P</b> 3215550142 <b>F</b> 3215550168 <b>E</b> info@hcfnet.example<br>
    <b>W</b> www.theharborviewfellowship.example</p>
  <div class="footer-art" role="img" aria-label="Faint illustration of raised-hand figures and a church"></div>
</section>

<section class="sheet letterhead" aria-label="Letterhead">
  <div class="brand"><span class="mark"></span>The Harborview Fellowship</div>
  <div class="side-rule"></div>
  <p class="address">218 Maple Crest Lane Alder Cove, OR 97999<br>
    <b>P</b> 3215550142 <b>F</b> 3215550168 <b>E</b> info@hcfnet.example<br>
    <b>W</b> www.theharborviewfellowship.example</p>
  <div class="footer-art" role="img" aria-label="Faint illustration of raised-hand figures and a church"></div>
</section>

<section class="sheet envelope" aria-label="Envelope">
  <div class="flap"></div>
  <div class="brand"><span class="mark"></span>The Harborview Fellowship</div>
  <p class="address">218 Maple Crest Lane Alder Cove, OR 97999<br>
    <b>www.theharborviewfellowship.example</b></p>
  <div class="footer-art" role="img" aria-label="Faint illustration of raised-hand figures and a church"></div>
</section>

<section class="sheet card-front" aria-label="Business card front">
  <p class="person"><b>Dalton M. Whitley</b><br>Lead Pastor</p>
  <div class="brand"><span class="mark"></span>The Harborview Fellowship</div>
  <p class="contact">218 Maple Crest Lane Alder Cove, OR 97999<br>
    P 3215550142 F 3215550168 E info@hcfnet.example<br>
    W www.theharborviewfellowship.example</p>
</section>

<section class="sheet card-back" aria-label="Business card back">
  <div class="brand"><span class="mark"></span>The Harborview Fellowship</div>
  <ul class="schedule">
    <li class="head">Service Schedule:</li>
    <li class="line">• Sunday Christian Training: 10:00 am</li>
    <li class="line">• Sunday Worship Service: 11:15 am</li>
    <li class="line">• Sunday Celebration Service: 6:30 pm</li>
    <li class="line">• Connection Groups (weekdays): 7:00 pm</li>
    <li class="line">• Children and Student activities provided</li>
    <li class="line">• Nursery provided</li>
  </ul>
</section>

</body>
</html>
```